Letterhead and Business Cards

Using our new logo we would like designs for the following,

1.Letterhead

2. 2 x Business Cards

I will need all three in high quality PDF files ready for printing. I will also require the top and bottom of the letterhead as two JPG files.

Target Market(s)

We are a business to business company dealing with middle to upper management both as clients and suppliers.

Industry/Entity Type

Business

Requirements
Must have
• 1. Look professional.
• 2. Utilise our logo colours
• 3. Incorporate our logo on both.
• 4. Letterhead

• Address:
• Pell Harrow Court
• Pell Harrow Lane
• London
• WC1R 4JZ

• Tel:0845 312 4096
• Fax: 0845 312 7158
• Website: www.kovimerlox.com
• Email: info@kovimerlox.com

• Directors: D.R. Marsh and H.J. Marsh Company Registration No: 52064918(This should be quite small in the letterhead footer somewhere)

• Business Card One Sided Only

• 1. Dominic R. Marsh
• Managing Director

• Address:
• Pell Harrow Court
• Pell Harrow Lane
• London
• WC1R 4JZ

• Tel:0845 312 4096
• Fax: 0845 312 7159
• Mob: 0791 526 3307
• Email: dominic@kovimerlox.com

• 2. Helen J. Marsh
• Sales Director

• Address:
• Pell Harrow Court
• Pell Harrow Lane
• London
• WC1R 4JZ

• Tel:0845 312 4096
• Fax: 0845 312 7158
• Mob: 0794 862 1190
• Email: helen@kovimerlox.com

• Please note some of this info may change for final printing.

```html
<!DOCTYPE html>
<html lang="en">
<head>
<meta charset="utf-8">
<title>Kovimerlox Stationery</title>
<link rel="stylesheet" href="https://fonts.googleapis.com/css2?family=Arimo:wght@400;700&family=Tinos&display=swap">
<style>
  :root {
    --brand-green: #74d02b;
    --brand-grey: #8f9da2;
    --ink: #111111;
    --paper: #ffffff;
    --backdrop: #f0f0f0;
    --shadow: rgba(0,0,0,0.18);
  }
  html, body {
    margin: 0;
    padding: 0;
    width: 1199px;
    height: 1200px;
    overflow: hidden;
    background: var(--backdrop);
    font-family: "Arimo", Arial, sans-serif;
  }
  .canvas { position: relative; width: 1199px; height: 1200px; }

  .sheet {
    position: absolute;
    background: var(--paper);
    box-shadow: 1px 2px 5px var(--shadow);
  }

  /* Letterhead */
  .letterhead { left: 79px; top: 61px; width: 763px; height: 1080px; }

  .brand {
    position: absolute;
    display: flex;
    flex-direction: column;
    align-items: center;
  }
  .brand-dot {
    border-radius: 50%;
    background: var(--brand-green);
  }
  .brand-name {
    font-weight: 700;
    color: var(--brand-grey);
    letter-spacing: -0.5px;
    line-height: 1;
  }
  .letterhead .brand { left: 72px; top: 44px; width: 205px; }
  .letterhead .brand-dot { width: 72px; height: 72px; margin-bottom: 10px; }
  .letterhead .brand-name { font-size: 32px; }

  .address {
    position: absolute;
    color: var(--brand-grey);
    font-size: 12.5px;
    line-height: 17.5px;
  }
  .letterhead .address { left: 88px; top: 168px; }

  .person {
    position: absolute;
    text-align: right;
    color: var(--brand-grey);
  }
  .person-name { color: var(--brand-green); font-weight: 700; }
  .letterhead .person { right: 91px; top: 55px; font-size: 13px; line-height: 16px; }

  .letter-body {
    position: absolute;
    left: 89px;
    width: 590px;
    font-family: "Tinos", "Times New Roman", serif;
    font-size: 15.2px;
    line-height: 18px;
    color: var(--ink);
  }
  .letter-body p { margin: 0; position: absolute; left: 0; width: 590px; }

  .contact {
    position: absolute;
    text-align: right;
    color: var(--brand-grey);
  }
  .contact .label { color: var(--brand-green); font-weight: 700; }
  .letterhead .contact { right: 91px; top: 927px; font-size: 13px; line-height: 18px; }

  .legal {
    position: absolute;
    right: 91px;
    top: 1016px;
    text-align: right;
    font-size: 7.5px;
    line-height: 9.5px;
    color: var(--brand-grey);
  }

  /* Business cards */
  .card { left: 808px; width: 310px; height: 201px; }
  .card-dominic { top: 223px; }
  .card-helen { top: 460px; }
  .card .brand { left: 19px; top: 24px; width: 142px; }
  .card .brand-dot { width: 48px; height: 48px; margin-bottom: 7px; }
  .card .brand-name { font-size: 22px; }
  .card .person { right: 28px; top: 35px; font-size: 11.5px; line-height: 15px; }
  .card .person-name { font-style: normal; }
  .card .address { left: 29px; top: 114px; font-size: 10.5px; line-height: 15px; }
  .card .contact { right: 28px; top: 86px; font-size: 10px; line-height: 18px; font-weight: 700; }
</style>
</head>
<body>
<div class="canvas">

  <section class="sheet letterhead">
    <div class="brand">
      <div class="brand-dot"></div>
      <div class="brand-name">Kovimerlox</div>
    </div>
    <div class="address">Pell Harrow Court<br>Pell Harrow Lane<br>London<br>WC1R 4JZ</div>
    <div class="person">
      <div class="person-name">Dominic R. Marsh</div>
      <div class="person-title">Managing Director</div>
    </div>

    <div class="letter-body">
      <p style="top:266px">Date</p>
      <p style="top:320px">Recipient Name<br>Company Name<br>Street Address<br>City, State, Postcode</p>
      <p style="top:428px">Dear Name Here,</p>
      <p style="top:463px">Nunc suscipit viverra augue, vel gravida nibh euismod a. Fusce fermentum massa sed nulla molestie vel facilisis nulla commodo. Cras in purus non magna dictum accumsan at quis tortor. Donec placerat nulla id nibh bibendum id sollicitudin libero convallis. Nam ac elementum sem.</p>
      <p style="top:550px">Etiam pharetra, diam sed rutrum semper, metus massa hendrerit purus, at lacinia eros augue vitae velit. Phasellus orci sapien, gravida ut pellentesque a, rhoncus quis ante. Nullam egestas augue orci.</p>
      <p style="top:624px">Maecenas quis quam enim, ac hendrerit dui. Suspendisse nec orci sed turpis suscipit molestie eu non augue. Donec eget lorem nec leo interdum feugiat. Aenean eu erat nisi, et euismod massa. Fusce porta, eros id vulputate dictum, neque erat consequat lacus, sed semper mauris mi id felis. Lorem ipsum dolor sit amet, consectetur adipiscing elit.</p>
      <p style="top:714px">Sincerely,</p>
      <p style="top:786px">Dominic R. Marsh<br>Managing Director</p>
    </div>

    <div class="contact">
      <div><span class="label">T:</span> 0845 312 4096</div>
      <div><span class="label">F:</span> 0845 312 7158</div>
      <div>www.kovimerlox.com</div>
      <div>info@kovimerlox.com</div>
    </div>
    <div class="legal">Directors: D.R. Marsh and H.J. Marsh<br>Company Registration No: 52064918</div>
  </section>

  <section class="sheet card card-dominic">
    <div class="brand">
      <div class="brand-dot"></div>
      <div class="brand-name">Kovimerlox</div>
    </div>
    <div class="person">
      <div class="person-name">Dominic R. Marsh</div>
      <div class="person-title">Managing Director</div>
    </div>
    <div class="contact">
      <div><span class="label">T:</span> 0845 312 4096</div>
      <div><span class="label">F:</span> 0845 312 7159</div>
      <div><span class="label">M:</span> 0791 526 3307</div>
      <div>www.kovimerlox.com</div>
      <div>dominic@kovimerlox.com</div>
    </div>
    <div class="address">Pell Harrow Court<br>Pell Harrow Lane<br>London<br>WC1R 4JZ</div>
  </section>

  <section class="sheet card card-helen">
    <div class="brand">
      <div class="brand-dot"></div>
      <div class="brand-name">Kovimerlox</div>
    </div>
    <div class="person">
      <div class="person-name">Helen J. Marsh</div>
      <div class="person-title">Sales Director</div>
    </div>
    <div class="contact">
      <div><span class="label">T:</span> 0845 312 4096</div>
      <div><span class="label">F:</span> 0845 312 7158</div>
      <div><span class="label">M:</span> 0794 862 1190</div>
      <div>www.kovimerlox.com</div>
      <div>helen@kovimerlox.com</div>
    </div>
    <div class="address">Pell Harrow Court<br>Pell Harrow Lane<br>London<br>WC1R 4JZ</div>
  </section>

</div>
</body>
</html>
```